Church needs a graphic design/flyer layout for upcoming series

I need a multi-purpose design for promoting both our upcoming series of messages and our fall kick-off event where we will launch the messages.

Our promotion will be printed on a two-sided. One side is simple and focuses on the series and the other side has details in regards to the event. I have provided an attachment example of what we did last time.

The design needs to be multi-purpose because it will be used for our sermon Power Points, placed on our website banner, social media, etc.

• Sermon series is called “Harbor Lanterns”
• The subtitle will be “What’s keeping you from God?”
• Our name logo should be on the graphic as well.
• The subject manner will revolve around common hurdles that people face about God and Christianity: The existence of God, the exclusivity of religion, Hell, the reliability of the Bible, Hypocrisy in the church, etc.
• Our mission is “Connecting Young Families to Christ” so our focus is to reach out to families while not being exclusive to others.
• Our target audience is families with school-aged kids.
• This series is an invitational focus so we want it to be appealing to non-church goers.
• It should be attention grabbing while not being too ‘edgy’

• The front of the card will most likely consist the Sermon Series Graphic, title & subtitle of the series, and perhaps our name logo somewhere on it.
• The back of the card will invite and give the basic information for the event so that the people will be encouraged to save the date and come to the event.
• Here are some things that could be included on that advertisement:
o The name of the event: “Westbrook Commons Open Day”
o The date and time of the event: Sept 23rd @ 10:30
o Features of the event:
 Free lunch
 Children’s program
 Bouncy Castle
 Start of the “Harbor Lanterns” messages.
 Sample of topics
o Information about the church: our website and address, etc
o Engaging pictures and graphics.
• The rest of the tone and manner are the same as the sermon series graphic.
The flyer will be 11X14, like a postcard size.

Target Market(s)

Young families who are spiritually curious but not committed church attenders.

Colors

Designer to choose colors to be used in the design.

Requirements
Nice to have
• A modern and professional looking design.
Should not have
• Anything offensive or not family friendly.

```html
<!DOCTYPE html>
<html lang="en">
<head>
<meta charset="utf-8">
<title>Harbor Lanterns – Postcard Front and Back</title>
<link href="https://fonts.googleapis.com/css2?family=Anton&family=Comic+Neue:wght@700&family=Source+Sans+3:wght@600&family=PT+Sans:wght@400&family=Tinos:wght@400;700&display=swap" rel="stylesheet">
<style>
  :root {
    --page-bg: #ebebeb;
    --orange: #f7941d;
    --purple: #92278f;
    --purple-light: #a23a9e;
    --blue: #0b74bd;
    --white: #ffffff;
    --logo-green: #6b7f73;
    --title-plate: rgba(90, 90, 90, 0.72);
    --photo-window: #f4f2ee;
    --photo-brick: #8c4e38;
    --photo-skin: #d6a07e;
    --photo-hair: #4a3328;
    --photo-dark: #262121;
    --photo-green: #5f9c74;
    --photo-yellow: #d9c94a;
  }
  * { box-sizing: border-box; margin: 0; padding: 0; }
  html, body { width: 1200px; height: 1200px; overflow: hidden; }
  body { background: var(--page-bg); position: relative; font-family: "Source Sans 3", sans-serif; }

  .card {
    position: absolute;
    left: 287px;
    width: 616px;
    height: 484px;
    box-shadow: 0 4px 8px rgba(0,0,0,0.25);
    overflow: hidden;
  }

  /* Front */
  .card--front { top: 102px; }
  .front-photo {
    position: absolute; inset: 0;
    background:
      radial-gradient(ellipse 26% 22% at 54% 70%, rgba(110,62,44,0.95) 0%, transparent 100%),
      radial-gradient(ellipse 18% 16% at 30% 58%, rgba(70,62,58,0.95) 0%, transparent 100%),
      radial-gradient(ellipse 14% 20% at 12% 38%, rgba(214,160,126,0.9) 0%, transparent 100%),
      radial-gradient(ellipse 12% 15% at 38% 32%, rgba(226,180,150,0.85) 0%, transparent 100%),
      radial-gradient(ellipse 12% 15% at 58% 26%, rgba(200,140,110,0.85) 0%, transparent 100%),
      radial-gradient(ellipse 12% 15% at 76% 34%, rgba(214,160,126,0.85) 0%, transparent 100%),
      radial-gradient(ellipse 14% 18% at 92% 30%, rgba(120,82,62,0.9) 0%, transparent 100%),
      radial-gradient(ellipse 8% 22% at 98% 52%, var(--photo-yellow) 0%, transparent 100%),
      radial-gradient(ellipse 8% 16% at 14% 62%, var(--photo-green) 0%, transparent 100%),
      radial-gradient(ellipse 30% 30% at 50% 48%, rgba(58,46,42,0.8) 0%, transparent 100%),
      radial-gradient(ellipse 22% 30% at 92% 8%, var(--photo-window) 0%, transparent 100%),
      radial-gradient(ellipse 20% 30% at 4% 10%, var(--photo-brick) 0%, transparent 100%),
      linear-gradient(180deg, #d8cfc6 0%, #a5806a 32%, #5a463e 62%, var(--photo-dark) 100%);
  }
  .series-plate {
    position: absolute; left: 101px; top: 22px;
    width: 406px; height: 68px;
    background: var(--title-plate);
    border: 1.5px solid var(--white);
    border-radius: 10px;
    display: flex; align-items: center; justify-content: center;
  }
  .series-title {
    font-family: "Anton", sans-serif; font-weight: 400;
    font-size: 56px; line-height: 1;
    color: var(--orange);
    -webkit-text-stroke: 1.5px var(--white);
    letter-spacing: 0.5px;
    white-space: nowrap;
  }
  .series-subtitle {
    position: absolute; left: 0; right: 0; top: 430px;
    text-align: center;
    font-family: "Comic Neue", cursive;
    font-weight: 700; font-size: 30px;
    color: var(--white);
    text-shadow: 0 1px 3px rgba(0,0,0,0.5);
  }

  /* Back */
  .card--back { top: 642px; background: var(--purple); }
  .back-frame {
    position: absolute; left: 6px; top: 6px; right: 6px; bottom: 70px;
    border: 1px solid rgba(255,255,255,0.35);
    border-bottom: none;
  }
  .event-name {
    position: absolute; left: 0; right: 0; top: 40px;
    text-align: center;
    font-family: "Comic Neue", cursive; font-weight: 700;
    font-size: 36px; color: var(--white); line-height: 1;
  }
  .event-date {
    position: absolute; left: 0; right: 0; top: 83px;
    text-align: center;
    font-family: "Tinos", serif; font-weight: 700;
    font-size: 33px; color: var(--white); line-height: 1;
  }
  .features-heading {
    position: absolute; left: 0; right: 0; top: 134px;
    text-align: center;
    font-family: "Tinos", serif; font-weight: 700;
    font-size: 31px; color: var(--orange); line-height: 1;
  }
  .feature {
    position: absolute; height: 37px;
    border: 1.5px solid var(--white);
    color: var(--white);
    font-family: "Source Sans 3", sans-serif; font-weight: 600;
    font-size: 21px;
    display: flex; align-items: center; justify-content: center;
    white-space: nowrap;
  }
  .feature::before { content: "•"; margin-right: 6px; font-size: 17px; }
  .feature--lunch { left: 49px; top: 180px; width: 138px; }
  .feature--kids { left: 195px; top: 180px; width: 212px; }
  .feature--castle { left: 414px; top: 180px; width: 175px; }
  .feature--series { left: 105px; top: 228px; width: 413px; }
  .feature--topics { left: 205px; top: 276px; width: 200px; }

  .church-name-block {
    position: absolute; left: 229px; top: 332px;
    width: 159px; height: 73px;
    background: var(--logo-green);
    border: 1.5px solid rgba(255,255,255,0.85);
    display: flex; flex-direction: column; align-items: center; justify-content: center; gap: 6px;
  }
  .church-name-dot { width: 28px; height: 28px; border-radius: 50%; background: var(--orange); }
  .church-name {
    font-family: "Source Sans 3", sans-serif; font-weight: 600; font-size: 11px;
    color: var(--white);
  }
  .kids-art {
    position: absolute; left: 429px; top: 300px;
    width: 180px; height: 122px;
    background:
      radial-gradient(ellipse 14% 16% at 20% 18%, #f2c9a0 0%, transparent 100%),
      radial-gradient(ellipse 12% 14% at 50% 36%, #f2c9a0 0%, transparent 100%),
      radial-gradient(ellipse 15% 18% at 82% 16%, #f5d76a 0%, transparent 100%),
      radial-gradient(ellipse 14% 16% at 20% 50%, #3fa6d8 0%, transparent 100%),
      radial-gradient(ellipse 12% 14% at 50% 62%, #8cc63f 0%, transparent 100%),
      radial-gradient(ellipse 15% 18% at 82% 55%, #f4e04d 0%, transparent 100%),
      radial-gradient(ellipse 10% 18% at 20% 84%, #d9443a 0%, transparent 100%),
      radial-gradient(ellipse 10% 12% at 50% 88%, #e85a4f 0%, transparent 100%),
      radial-gradient(ellipse 10% 14% at 82% 86%, #b03aa8 0%, transparent 100%),
      radial-gradient(ellipse at 50% 60%, #b24fae 0%, var(--purple-light) 50%, var(--purple) 100%);
  }

  .contact-band {
    position: absolute; left: 0; right: 0; bottom: 0; height: 64px;
    background: var(--blue);
    border-top: 3px solid #3a66b8;
    border-bottom: 2px solid var(--orange);
    color: var(--white);
    font-family: "Tinos", serif;
    text-align: center;
  }
  .contact-address { margin-top: 9px; font-size: 19px; font-weight: 700; line-height: 1.1; }
  .contact-lines {
    margin-top: 3px; display: flex; justify-content: center; gap: 8px;
    font-size: 13px; font-weight: 400; font-family: "Tinos", serif;
  }
  .contact-item { display: flex; align-items: center; gap: 3px; }
  .contact-item svg { width: 13px; height: 13px; }
</style>
</head>
<body>

<section class="card card--front">
  <div class="front-photo" role="img" aria-label="Photo of a smiling group of friends standing in a circle with arms around each other"></div>
  <div class="series-plate"><h1 class="series-title">HARBOR LANTERNS</h1></div>
  <p class="series-subtitle">What’s keeping you from God?</p>
</section>

<section class="card card--back">
  <div class="back-frame"></div>
  <h2 class="event-name">Westbrook Commons Open Day</h2>
  <p class="event-date">Date: Sept 23rd @ 10:30</p>
  <h3 class="features-heading">Features of the event:</h3>

  <div class="feature feature--lunch">Free lunch</div>
  <div class="feature feature--kids">Children’s program</div>
  <div class="feature feature--castle">Bouncy Castle</div>
  <div class="feature feature--series">Start of the “Harbor Lanterns” messages.</div>
  <div class="feature feature--topics">Sample of topics</div>

  <div class="church-name-block">
    <span class="church-name-dot"></span>
    <span class="church-name">Westbrook Commons Church</span>
  </div>
  <div class="kids-art" role="img" aria-label="Cartoon illustration of three children holding hands"></div>

  <footer class="contact-band">
    <p class="contact-address">Location: 1180 Maple Harbor Road, Lakeview, ON L0X 2B4</p>
    <div class="contact-lines">
      <span class="contact-item">
        <svg viewBox="0 0 16 16"><circle cx="8" cy="8" r="8" fill="#fff"/><path d="M5 4.5l1.5-.5 1 2-1 .8a5 5 0 0 0 2.7 2.7l.8-1 2 1-.5 1.5c-3.5.3-6.8-3-6.5-6.5z" fill="#0b74bd"/></svg>
        555.014.2290
      </span>
      <span class="contact-item">
        <svg viewBox="0 0 16 16"><circle cx="8" cy="8" r="8" fill="#fff"/><rect x="4" y="5" width="8" height="6" fill="none" stroke="#0b74bd" stroke-width="1.2"/><path d="M4 5l4 3.5L12 5" fill="none" stroke="#0b74bd" stroke-width="1.2"/></svg>
        hello@westbrookcommons.org
      </span>
      <span class="contact-item">
        <svg viewBox="0 0 16 16"><circle cx="8" cy="8" r="8" fill="#fff"/><circle cx="8" cy="8" r="4.8" fill="none" stroke="#0b74bd" stroke-width="1"/><ellipse cx="8" cy="8" rx="2" ry="4.8" fill="none" stroke="#0b74bd" stroke-width="1"/><path d="M3.2 8h9.6" stroke="#0b74bd" stroke-width="1"/></svg>
        www.westbrookcommons.org
      </span>
    </div>
  </footer>
</section>

</body>
</html>
```